VS Business Card

Design new business cards for VELNAstack

Please see attached for the design brief

**** Please note, please feel free to propose a font that works for a professional, technology company ***

Target Market(s)

Technology buyers

Industry/Entity Type

Business

```html
<!DOCTYPE html>
<html lang="en">
<head>
<meta charset="utf-8">
<title>VELNAstack Business Card</title>
<link rel="stylesheet" href="https://fonts.googleapis.com/css2?family=Barlow:wght@400;500;600&display=swap">
<style>
  :root {
    --page: #e8e8ea;
    --ink-navy: #21233a;
    --brand-navy: #2b3467;
    --brand-blue: #4a6fb5;
    --accent-orange: #e9a02a;
    --card-white: #f7f7f6;
    --text-dark: #2a2b33;
    --label: #3b4476;
  }
  html, body {
    margin: 0;
    width: 1200px;
    height: 800px;
    overflow: hidden;
    background: var(--page);
    font-family: "Barlow", Arial, sans-serif;
  }
  .canvas { position: relative; width: 1200px; height: 800px; }
  .card {
    position: absolute;
    width: 478px;
    height: 306px;
    box-sizing: border-box;
  }
  .corner-mark {
    position: absolute;
    top: 0;
    right: 0;
    width: 22px;
    height: 22px;
  }

  /* Front */
  .card-front { left: 376px; top: 74px; background: var(--ink-navy); }
  .card-front .corner-mark { background: var(--accent-orange); }
  .front-brand {
    position: absolute;
    left: 0; right: 0; top: 124px;
    display: flex; justify-content: center; align-items: center; gap: 14px;
  }
  .brand-square { width: 22px; height: 22px; background: var(--brand-blue); }
  .front-brand .brand-name {
    font-size: 44px; font-weight: 500; color: var(--brand-blue); letter-spacing: 0.5px;
  }
  .tagline-rule {
    position: absolute; left: 135px; width: 206px; top: 247px; height: 2px;
    background: var(--accent-orange);
  }
  .tagline {
    position: absolute; left: 0; right: 0; top: 256px; margin: 0;
    text-align: center; font-size: 16px; color: var(--accent-orange);
  }

  /* Back */
  .card-back { left: 374px; top: 418px; background: var(--card-white); }
  .card-back .corner-mark { background: var(--brand-blue); }
  .back-brand {
    position: absolute; left: 22px; top: 36px;
    display: flex; align-items: center; gap: 12px;
  }
  .back-brand .brand-square { background: var(--brand-navy); }
  .back-brand .brand-name {
    font-size: 42px; font-weight: 500; color: var(--brand-navy); letter-spacing: 0.5px;
  }
  .person {
    position: absolute; left: 36px; top: 138px; margin: 0;
    font-size: 18px; color: var(--brand-navy);
  }
  .person .role { font-size: 14px; margin-left: 8px; }
  .contact-list {
    position: absolute; left: 36px; top: 195px; margin: 0;
    display: grid; grid-template-columns: 49px auto; row-gap: 0;
    font-size: 13.5px; line-height: 16.8px;
  }
  .contact-list dt { color: var(--label); }
  .contact-list dd { margin: 0; color: var(--text-dark); }
  .company-address {
    position: absolute; left: 302px; top: 195px;
    font-style: normal; font-size: 13.5px; line-height: 16.8px; color: var(--text-dark);
  }
  .company-address .web {
    display: inline-block; font-weight: 600;
    padding-bottom: 2px; border-bottom: 2px solid var(--accent-orange);
  }
</style>
</head>
<body>
<main class="canvas">
  <section class="card card-front" aria-label="Card front">
    <div class="corner-mark"></div>
    <div class="front-brand">
      <span class="brand-square"></span>
      <span class="brand-name">VELNAstack</span>
    </div>
    <div class="tagline-rule"></div>
    <p class="tagline">… PROGRESS is our craft!</p>
  </section>

  <section class="card card-back" aria-label="Card back">
    <div class="corner-mark"></div>
    <div class="back-brand">
      <span class="brand-square"></span>
      <span class="brand-name">VELNAstack</span>
    </div>
    <p class="person">Martin Orel<span class="role">CEO</span></p>
    <dl class="contact-list">
      <dt>phone</dt><dd>+41 44 620 4810</dd>
      <dt>direct</dt><dd>+41 44 620 4811</dd>
      <dt>fax</dt><dd>+41 800 004 935</dd>
      <dt>mobile</dt><dd>+41 79 352 1764</dd>
      <dt>email</dt><dd>martin.orel@velnastack.io</dd>
    </dl>
    <address class="company-address">
      VELNAstack Solutions AG<br>
      Talweg 8<br>
      8400 Winterthur<br>
      Switzerland<br>
      <span class="web">www.velnastack.io</span>
    </address>
  </section>
</main>
</body>
</html>
```